依頼詳細
屋外にタペストリーで掲げている店案内ですが、ショッピングセンター内にあるため屋外からエステだと一目でわかるものにしたいと考えております。そのためのデザインをお願いいたします。
記載項目
記載項目
特にエステティックであることをはっきりと掲載したいため「ロゴマーク」「エステティックサロン」「美顔」「痩身」「脱毛」というワードを大きく
続いて「電話番号」「営業時間」
また「店名」も掲載しますが目立たなくとも良いです。
ロゴマークは添付のものをご利用ください。
色ならびにロゴマーク中のグラデーションの変更はしないようにお願いいたします。
参考として旧タペストリーと他店の駐車場看板を添付します。
旧タペストリーのデザインとは全くかけ離れて構いません。
駐車場看板は見せ方の参考として添付します。店名よりもエステティックを強調しているという事の参考になればと思います。

店名 ルフィナ鯖江店
電話番号 0778-41-6093
営業時間 9:30~20:30
サイズ:縦2400mm×横3200mm
希望イメージ
シンプル 複雑
単色 カラフル
暗い 明るい
日常 高級
遊び心 厳粛
未来的 伝統的
女性的 男性的
希望する色
設定なし
納品ファイル
• イラストレーター形式 (.ai)
• フォトショップ形式 (.psd)
補足説明
写真利用の場合は、納品の際は埋め込みではなくリンクでお願いします。
表記につきまして若干変更をさせていただきます、

「エステティックサロン」は英字よりカナ表記が目立つようにお願いいたします。
「美顔」→「フェイシャル」に変更(カナ表記)
「痩身」→「ボディ」に変更(カナ表記)
「脱毛」→変更なし

また女性の画像等はイメージやパーツとして使用いただいてもOKですが、スワンのマークをもう少し前面に出していただけたらと思います。
画像のイメージが前面にでるより、スワンのロゴが前面にでるようにできればと思います。イメージ画像等は全くないものでも可です。

添付でスワンのロゴのみのaiを追加いたします。

締め切りを変更させていただきます。

当方が伝えたいものが、しっかりと出ていて、色味も落ち着きがありながらロゴがはっきりと見えるデザインで好感が持てました。

本当にたくさんのデザインを頂きありがとうございます。

```html
<!DOCTYPE html>
<html lang="ja">
<head>
<meta charset="utf-8">
<title>Esthetic Salon Tapestry</title>
<link rel="stylesheet" href="https://fonts.googleapis.com/css2?family=Cormorant+Garamond:wght@500;600&family=Noto+Serif+JP:wght@500;600&family=Noto+Sans+JP:wght@400;500&display=swap">
<style>
  :root {
    --frame-dark: #2a1d17;
    --frame-line: #f4ede6;
    --panel-light: #fbf1ef;
    --panel-pink: #f3d9d8;
    --gold: #b58a5c;
    --gold-deep: #9a6f45;
    --band: rgba(176, 128, 92, 0.55);
    --ink: #3a2a24;
    --brand-red: #d24b57;
    --skin-light: #f1d3c4;
    --skin-mid: #e2b29c;
    --flower-pink: #f2b9bd;
  }
  * { margin: 0; padding: 0; box-sizing: border-box; }
  html, body {
    width: 1200px; height: 900px; overflow: hidden;
    background: var(--frame-dark);
  }
  .tapestry {
    position: relative; width: 1200px; height: 900px;
    background: var(--frame-dark);
  }
  .panel {
    position: absolute; left: 34px; top: 34px; right: 34px; bottom: 34px;
    border: 4px solid var(--frame-line);
    background: linear-gradient(120deg, var(--panel-light) 0%, #f8e6e4 45%, var(--panel-pink) 100%);
    overflow: hidden;
  }
  .photo-area {
    position: absolute; left: 470px; top: 0; right: 0; bottom: 0;
    background:
      radial-gradient(ellipse 45% 55% at 20% 75%, var(--flower-pink) 0%, rgba(242,185,189,0) 70%),
      linear-gradient(90deg, rgba(241,211,196,0) 0%, var(--skin-light) 35%, var(--skin-mid) 75%, #c99580 100%);
  }
  .title-word {
    position: absolute;
    font-family: "Cormorant Garamond", serif;
    font-weight: 600;
    color: var(--gold);
    line-height: 1;
    letter-spacing: 2px;
  }
  .title-esthetic { left: 58px; top: 48px; font-size: 178px; }
  .title-salon { left: 62px; top: 294px; font-size: 178px; }
  .kana-band {
    position: absolute; left: 0; top: 240px; width: 600px; height: 50px;
    background: linear-gradient(90deg, var(--band) 0%, rgba(176,128,92,0.45) 75%, rgba(176,128,92,0) 100%);
  }
  .kana-label {
    position: absolute; left: 68px; top: 242px;
    font-family: "Noto Serif JP", serif; font-weight: 500;
    font-size: 33px; letter-spacing: 9px; color: #fff;
  }
  .service {
    position: absolute; top: 542px;
    font-family: "Noto Serif JP", serif; font-weight: 600;
    color: var(--gold-deep); line-height: 1;
    padding: 14px 26px 14px 16px;
    background: radial-gradient(ellipse at center, rgba(255,255,255,0.85) 0%, rgba(255,255,255,0) 75%);
  }
  .service .lead { font-size: 66px; }
  .service .tail { font-size: 50px; }
  .service-face { left: 56px; }
  .service-body { left: 300px; }
  .service-hair { left: 540px; }
  .store-info {
    position: absolute; left: 64px; top: 660px;
    font-family: "Noto Sans JP", sans-serif; color: var(--ink);
  }
  .store-name { font-size: 22px; font-weight: 400; }
  .store-phone {
    display: flex; align-items: center; gap: 6px;
    margin-top: 6px; font-size: 34px; font-weight: 500; letter-spacing: 1px;
  }
  .store-hours { margin-top: 4px; font-size: 20px; }
  .brand {
    position: absolute; left: 720px; top: 700px;
    display: flex; align-items: center; gap: 18px;
    color: var(--brand-red);
    font-family: "Cormorant Garamond", serif; font-weight: 600;
  }
  .brand-dot {
    width: 74px; height: 74px; border-radius: 50%;
    background: var(--brand-red);
  }
  .brand-tagline { font-size: 24px; letter-spacing: 1px; }
  .brand-name { font-size: 62px; line-height: 1; letter-spacing: 3px; }
</style>
</head>
<body>
<main class="tapestry">
  <section class="panel">
    <div class="photo-area" role="img" aria-label="Soft-focus beauty photo of a woman's face beside pink flowers"></div>

    <div class="kana-band"></div>
    <h1 class="title-word title-esthetic">Esthetic</h1>
    <p class="kana-label">エステティックサロン</p>
    <p class="title-word title-salon">Salon</p>

    <p class="service service-face"><span class="lead">美</span><span class="tail">顔</span></p>
    <p class="service service-body"><span class="lead">痩</span><span class="tail">身</span></p>
    <p class="service service-hair"><span class="lead">脱</span><span class="tail">毛</span></p>

    <div class="store-info">
      <p class="store-name">ルフィナ鯖江店</p>
      <p class="store-phone">
        <svg width="28" height="24" viewBox="0 0 28 24" aria-hidden="true">
          <path d="M3 8 Q14 0 25 8 L22 12 L18 9 L18 7 Q14 5 10 7 L10 9 L6 12 Z" fill="#3a2a24"/>
          <rect x="6" y="12" width="16" height="10" rx="2" fill="#3a2a24"/>
          <circle cx="14" cy="17" r="3" fill="#fbf1ef"/>
        </svg>
        0778-41-6093
      </p>
      <p class="store-hours">〔営業時間〕AM9:30-PM8:30</p>
    </div>

    <div class="brand">
      <span class="brand-dot"></span>
      <div>
        <p class="brand-tagline">Esthetic salon</p>
        <p class="brand-name">CORALIE</p>
      </div>
    </div>
  </section>
</main>
</body>
</html>
```